Design for Certificate

Design a certificate for training, providing our company logo such as attachments. Company's name is "BRYNE Fjellvik Advisory Ltd", please refer to our company profile: https://www.bryne-fjellvik.example/company_info

The style of the current certificate is also attached, and another certificate of another company can be referred to. Psd & jpg are required for the final draft (the layers of psd are not merged). Thanks!

```html
<!DOCTYPE html>
<html lang="en">
<head>
<meta charset="utf-8">
<title>Certificate of Completion – BRYNE Fjellvik</title>
<link rel="stylesheet" href="https://fonts.googleapis.com/css2?family=Fira+Sans:wght@300;400;600;700&family=Playfair+Display:wght@700&display=swap">
<style>
  :root {
    --charcoal: #37383a;
    --charcoal-deep: #2e2f31;
    --cream: #fbf3ec;
    --cream-tint: #f6e6d8;
    --gold-light: #e8bd7e;
    --gold: #c98f3a;
    --rose-gold: #dfb796;
    --ink: #2f3032;
    --white: #ffffff;
  }
  * { margin: 0; padding: 0; box-sizing: border-box; }
  html, body {
    width: 1200px;
    height: 849px;
    overflow: hidden;
    background: var(--charcoal);
  }
  .certificate {
    position: relative;
    width: 1200px;
    height: 849px;
    overflow: hidden;
    background: radial-gradient(circle at 30% 40%, var(--charcoal) 0%, var(--charcoal-deep) 100%);
    font-family: "Fira Sans", sans-serif;
    color: var(--ink);
  }
  .certificate-sheet {
    position: absolute;
    inset: 0;
  }
  .text {
    position: absolute;
    white-space: nowrap;
    line-height: 1;
  }
  .centered { transform: translateX(-50%); }
  .title {
    left: 59px; top: 40px;
    font-family: "Playfair Display", serif;
    font-weight: 700;
    font-size: 54px;
    color: var(--rose-gold);
    text-shadow: 2px 3px 3px rgba(0,0,0,0.35);
    letter-spacing: -0.5px;
  }
  .awarded {
    left: 479px; top: 136px;
    font-weight: 300;
    font-size: 27px;
    letter-spacing: 0.5px;
  }
  .rule {
    position: absolute;
    height: 1px;
    background: var(--ink);
  }
  .rule-name { left: 187px; top: 283px; width: 667px; }
  .completed {
    left: 523px; top: 296px;
    font-weight: 300;
    font-size: 19px;
  }
  .course-name {
    left: 617px; top: 433px;
    font-weight: 600;
    font-size: 44px;
    color: var(--rose-gold);
  }
  .course-type {
    left: 617px; top: 482px;
    font-weight: 300;
    font-size: 35px;
  }
  .course-date {
    left: 355px; top: 592px;
    font-weight: 300;
    font-size: 20px;
  }
  .rule-date { left: 568px; top: 614px; width: 507px; }
  .issuer {
    left: 571px; top: 720px;
    font-weight: 600;
    font-size: 38px;
  }
  .rule-signature { left: 762px; top: 763px; width: 337px; }
  .signatory {
    left: 932px; top: 772px;
    font-weight: 300;
    font-size: 15px;
  }
  .number-label {
    left: 1026px; top: 18px;
    font-family: "Playfair Display", serif;
    font-size: 19px;
    color: var(--white);
  }
  .number-field {
    position: absolute;
    left: 874px; top: 50px;
    width: 310px; height: 45px;
    background: var(--white);
    border: 3px solid var(--gold-light);
  }
  .brand-name {
    font-weight: 600;
    color: var(--rose-gold);
    letter-spacing: 4px;
  }
  .brand-name-top {
    left: 1065px; top: 232px;
    font-size: 54px;
  }
  .brand-mark-corner {
    position: absolute;
    left: 62px; top: 560px;
    width: 150px; height: 150px;
    display: flex;
    flex-direction: column;
    align-items: center;
    justify-content: center;
    gap: 18px;
  }
  .brand-mark-corner .brand-square {
    width: 22px; height: 22px;
    background: var(--rose-gold);
  }
  .brand-mark-corner .brand-name {
    position: static;
    font-size: 34px;
    letter-spacing: 3px;
  }
</style>
</head>
<body>
<main class="certificate">
  <svg class="certificate-sheet" width="1200" height="849" viewBox="0 0 1200 849" aria-hidden="true">
    <defs>
      <linearGradient id="gold-edge" x1="0" y1="0" x2="1" y2="1">
        <stop offset="0" stop-color="#f0c58a"/>
        <stop offset="0.5" stop-color="#c98f3a"/>
        <stop offset="1" stop-color="#e8bd7e"/>
      </linearGradient>
      <linearGradient id="sheet-fill" x1="0" y1="0" x2="1" y2="1">
        <stop offset="0" stop-color="#fbf3ec"/>
        <stop offset="1" stop-color="#f8ebe0"/>
      </linearGradient>
    </defs>
    <path class="sheet-border" fill="url(#gold-edge)"
      d="M4,0 C48,190 190,310 250,525 C290,685 330,785 366,849 L1200,849 C1172,700 1112,598 1052,516 C972,400 892,250 842,0 Z"/>
    <path class="sheet-paper" fill="url(#sheet-fill)"
      d="M18,12 C60,190 200,310 262,522 C302,682 342,782 382,849 L1186,849 C1156,704 1098,604 1040,522 C960,404 880,256 826,12 Z"/>
  </svg>

  <h1 class="text title">CERTIFICATE of Completion</h1>
  <p class="text centered awarded">This certificate is awarded to</p>
  <div class="rule rule-name"></div>
  <p class="text centered completed">has successfully completed</p>

  <h2 class="text centered course-name">Brand Reputation Management</h2>
  <p class="text centered course-type">Training Course</p>

  <p class="text course-date">Sixteen hours, held on</p>
  <div class="rule rule-date"></div>

  <p class="text centered issuer">BRYNE Fjellvik</p>
  <div class="rule rule-signature"></div>
  <p class="text centered signatory">Chief Technology Officer</p>

  <p class="text centered number-label">Certificate №</p>
  <div class="number-field"></div>

  <p class="text centered brand-name brand-name-top">BRYNE</p>

  <div class="brand-mark-corner">
    <span class="brand-square"></span>
    <span class="brand-name">BRYNE</span>
  </div>
</main>
</body>
</html>
```